US Based Startup requires Website Design for Kavrelon Cell

We are launching a battery technology called "Kavrelon Cell" for which we need an elegant website design. We use red and black to represent positive and negative node color used in battery. The background is white. The font must provide more wide space and easy to read.
Kavrelon CellTM is a technology that uses fast switches, such as transistor switches, to make batteries more efficient. The novel technology can be implemented in all types of batteries – including non-rechargeable batteries, rechargeable batteries, wet-cell batteries and all metal oxide batteries.
Normal batteries are “non-switching”, that is, these batteries can only be connected to one another in parallel or series connections. Parallel connections enable batteries to charge faster whilst series connections enable the battery to discharge more efficiently to the load.
Kavrelon CellTM technology enables batteries to be connected in a third connection method called “vexa-loopTM” that combines the benefit of faster charging of the batteries with renewable energy source, such as solar, in parallel connection, and then quickly re-configures the same batteries using the fast transistor switches, to be connected in series with the load, to discharge efficiently.

Target Market(s)

Renewable energy

Industry/Entity Type

Renewable

Coding

Coded - Design and coding required

Number of Pages Required

5+ page

Requirements
Must have
• The primary colors are red and black for logo and fonts. The background is white.
The font must be easy to read type of fonts with more white space. Only pictures will be in full color.
Nice to have
• Elegant and simple design bringing out a new battery concept to the energy industry.

```html
<!DOCTYPE html>
<html lang="en">
<head>
<meta charset="utf-8">
<title>Kavrelon Cell</title>
<link href="https://fonts.googleapis.com/css2?family=Open+Sans:wght@400;600;700;800&family=Montserrat:wght@800;900&display=swap" rel="stylesheet">
<style>
:root{
  --red:#e11f26;
  --red-dark:#c4161c;
  --ink:#222;
  --text:#555;
  --muted:#888;
  --dark:#252525;
  --pale:#f6f6f6;
  --white:#fff;
}
*{margin:0;padding:0;box-sizing:border-box}
html,body{width:1200px;height:4812px;overflow:hidden}
body{font-family:"Open Sans",sans-serif;color:var(--ink);background:var(--white);position:relative}
.abs{position:absolute}
.nav{top:0;left:0;width:1200px;height:94px;background:var(--white)}
.nav a{position:absolute;top:0;height:94px;line-height:102px;font-size:16px;font-weight:600;color:var(--ink);text-decoration:none}
.nav a.active{background:var(--red);color:var(--white);left:172px;width:149px;text-align:center}
.hero{top:94px;left:0;width:1200px;height:800px;background:linear-gradient(180deg,#dfe8f2 0%,#eef3f8 60%,#fff 100%)}
.brand{left:215px;top:290px;display:flex;align-items:center;gap:30px}
.brand-dot{width:90px;height:90px;border-radius:50%;background:var(--red)}
.brand-name{font-family:"Montserrat",sans-serif;font-weight:900;color:var(--ink);font-size:92px;line-height:.98;letter-spacing:1px}
.swoosh{left:0;top:0}
h2.sec{font-size:30px;font-weight:700;color:var(--ink);line-height:1.2}
h2.sec span,.red{color:var(--red)}
.about-title{left:172px;top:896px}
.about-text{left:172px;top:955px;width:478px;font-size:11.5px;line-height:22px;color:var(--text);text-align:justify}
.about-text p{margin-bottom:10px}
.btn{display:inline-block;background:var(--red);color:var(--white);font-weight:700;font-size:15px;text-align:center;border-radius:6px}
.about-btn{left:172px;top:1168px;width:132px;height:56px;line-height:56px}
.about-img{left:729px;top:910px;width:471px;height:260px;border-radius:30px;background:radial-gradient(ellipse at 50% 40%,#2b74d8 0%,#1742a8 45%,#c9d8ee 80%,#fff 100%)}
.services{top:1380px;left:0;width:1200px;height:745px;background:linear-gradient(180deg,#eef0f3 0%,#dadde2 70%,#cfd2d7 100%)}
.svc-head{left:0;top:1490px;width:1200px;text-align:center}
.svc-head .l1{font-size:30px;font-weight:700;color:var(--ink)}
.svc-head .l2{font-size:28px;font-weight:700;color:var(--red);margin-top:2px}
.card{background:var(--white);border-radius:14px;box-shadow:0 6px 22px rgba(0,0,0,.12);text-align:center}
.svc-card{top:1700px;width:271px;height:318px}
.svc-card h3{margin-top:110px;font-size:20px;font-weight:600;letter-spacing:.5px}
.svc-card p{font-size:12px;line-height:22px;color:var(--text);padding:0 18px;margin-top:10px}
.svc-card .pill{display:inline-block;margin-top:20px;width:118px;height:46px;line-height:46px;border-radius:23px;background:#333;color:#fff;font-size:13px;font-weight:700}
.svc-card .pill.on{background:var(--red)}
.svc-icon{width:152px;height:152px;border-radius:50%;border:6px solid #fff;box-shadow:0 4px 14px rgba(0,0,0,.2);position:absolute;left:50%;margin-left:-76px;top:-76px;background:#333;display:flex;align-items:center;justify-content:center}
.svc-icon.on{background:var(--red)}
.feat-img{left:40px;top:2380px;width:420px;height:235px;border-radius:22px;background:linear-gradient(180deg,#4a8fe0 0%,#9cc9f0 45%,#5b9b3c 75%,#2e3b4c 100%)}
.feat-title{left:623px;top:2254px;font-size:30px;font-weight:600;line-height:42px}
.feat-item{width:362px}
.feat-item h4{font-size:24px;font-weight:700;color:var(--red)}
.feat-item p{font-size:13px;line-height:22px;color:var(--text);text-align:justify;margin-top:6px}
.solutions{top:2860px;left:0;width:1200px;height:766px;background:var(--pale)}
.sol-title{left:172px;top:3000px;font-size:32px;line-height:40px}
.sol-lead{left:172px;top:3095px;width:230px;font-size:12px;line-height:20px;color:var(--text)}
.more{font-size:12px;font-weight:600;color:var(--red)}
.sol-card{width:270px;height:280px;background:var(--white);padding:18px 16px}
.sol-card .num{position:absolute;right:18px;top:8px;font-size:100px;font-weight:800;color:#f1f1f1;line-height:1}
.sol-card .ic{position:relative;width:48px;height:48px}
.sol-card h5{position:relative;font-size:19px;font-weight:600;margin-top:22px}
.sol-card p{position:relative;font-size:12px;line-height:21px;color:var(--muted);margin-top:10px;text-align:justify}
.sol-card .more{position:relative;display:block;margin-top:16px}
.blog-title{left:0;top:3712px;width:1200px;text-align:center}
.blog-card{top:3786px;width:276px;height:336px;background:var(--white);box-shadow:0 3px 16px rgba(0,0,0,.1);text-align:center}
.blog-photo{position:absolute;left:6px;top:6px;width:264px;height:176px;background:linear-gradient(135deg,#24384a,#5f7f96 55%,#1b2a38)}
.blog-photo.b{background:linear-gradient(135deg,#1e2c33,#7a8d96 55%,#27343b)}
.blog-photo.c{background:linear-gradient(135deg,#c9d2da,#f0a860 50%,#8aa0b4)}
.date{position:absolute;left:20px;top:16px;width:50px;height:50px;border-radius:50%;background:var(--red);color:#fff;font-size:11px;font-weight:600;line-height:15px;padding-top:9px}
.blog-card h6{position:absolute;left:20px;right:20px;top:202px;font-size:14px;font-weight:700;line-height:20px}
.blog-card p{position:absolute;left:22px;right:22px;top:256px;font-size:11px;line-height:19px;color:var(--muted)}
.load-btn{left:543px;top:4110px;width:116px;height:50px;line-height:50px;font-size:14px}
.footer{top:4360px;left:0;width:1200px;height:452px;background:var(--dark)}
.foot-brand{left:172px;top:4528px;display:flex;align-items:center;gap:14px}
.foot-brand .dot{width:30px;height:30px;border-radius:50%;background:var(--red)}
.foot-brand .name{font-family:"Montserrat",sans-serif;font-weight:800;color:#fff;font-size:27px;line-height:30px}
.foot-h{font-size:18px;font-weight:700;color:#fff;line-height:26px}
.links{left:495px;top:4505px;list-style:none;font-size:14px;line-height:25px;color:#ddd}
.email{left:705px;top:4530px;width:322px;height:46px;background:#fff;border-radius:4px;font-size:14px;color:#555;padding:13px 12px}
.sub{left:705px;top:4612px;width:112px;height:48px;line-height:48px;font-size:14px;border-radius:4px}
.copy{left:0;top:4752px;width:1200px;text-align:center;font-size:13px;color:#fff;padding-left:240px}
</style>
</head>
<body>

<nav class="nav abs">
  <a class="active" href="#">HOME</a>
  <a href="#" style="left:355px">ABOUT US</a>
  <a href="#" style="left:495px">SERVICES</a>
  <a href="#" style="left:632px">FEATURES</a>
  <a href="#" style="left:770px">BLOG</a>
  <a href="#" style="left:877px">CONTACT US</a>
</nav>

<section class="hero abs"></section>
<div class="brand abs">
  <div class="brand-dot"></div>
  <div class="brand-name">KAVRELON<br>CELL™</div>
</div>
<svg class="swoosh abs" width="1200" height="900" viewBox="0 0 1200 900">
  <path d="M0 860 Q420 715 1160 692 L1160 716 Q440 745 0 885 Z" fill="var(--red)"/>
  <circle cx="1162" cy="704" r="21" fill="var(--red)"/>
</svg>

<h2 class="sec abs about-title">ABOUT <span>KAVRELON CELL</span></h2>
<div class="about-text abs">
  <p>Nam libero tempore, cum soluta nobis est eligendi optio cumque nihil impedit quo minus id quod maxime placeat facere possimus, omnis voluptas assumenda est, omnis dolor repellendus. Temporibus autem quibusdam et aut officiis debitis aut rerum necessitatibus saepe eveniet ut et voluptates repudiandae sint et molestiae non recusandae.</p>
  <p>At vero eos et accusamus et iusto odio dignissimos ducimus qui blanditiis praesentium voluptatum deleniti atque corrupti quos dolores et quas molestias excepturi sint oc caecati cupiditate non provident.</p>
</div>
<a class="btn abs about-btn">READ MORE</a>
<div class="about-img abs" role="img" aria-label="Battery cell filled with solar panels and wind turbines"></div>

<section class="services abs"></section>
<svg class="abs" style="left:0;top:1300px" width="1200" height="110" viewBox="0 0 1200 110">
  <path d="M0 0 H1200 V20 Q700 95 0 100 Z" fill="#fff"/>
</svg>
<div class="svc-head abs"><div class="l1">OUR</div><div class="l2">KAVRELON CELL SERVICES</div></div>

<div class="card svc-card abs" style="left:172px">
  <div class="svc-icon"><svg width="40" height="56" viewBox="0 0 40 56" fill="none" stroke="#fff" stroke-width="3"><rect x="8" y="8" width="24" height="44" rx="3"/><rect x="15" y="3" width="10" height="5"/><path d="M22 18 L16 31 H24 L18 44" stroke-linejoin="round"/></svg></div>
  <h3>LITHIUM ION BATTERY</h3>
  <p>aut reiciendis voluptatibus maiores alias consequatur aut perferendis doloribus as periores repellat.</p>
  <span class="pill">READ MORE</span>
</div>
<div class="card svc-card abs" style="left:463px">
  <div class="svc-icon on"><svg width="64" height="50" viewBox="0 0 64 50" fill="none" stroke="#fff" stroke-width="3"><rect x="4" y="10" width="56" height="30" rx="3"/><rect x="12" y="18" width="18" height="14"/><path d="M46 16 L40 26 H48 L42 36"/><path d="M10 40 V46 M54 40 V46 M20 4 H44 V10"/></svg></div>
  <h3 class="red">SOLION INVERTER</h3>
  <p>aut reiciendis voluptatibus maiores alias consequatur aut perferendis doloribus as periores repellat.</p>
  <span class="pill on">READ MORE</span>
</div>
<div class="card svc-card abs" style="left:755px">
  <div class="svc-icon"><svg width="62" height="60" viewBox="0 0 62 60" fill="none" stroke="#fff" stroke-width="2.5"><circle cx="31" cy="12" r="6"/><path d="M31 1V3M31 21V23M20 12H22M40 12H42M23 4L25 6M37 18L39 20M39 4L37 6M25 18L23 20"/><path d="M10 30H52L58 46H4Z M18 30L14 46M31 30V46M44 30L48 46M7 38H55M31 46V56M22 56H40"/></svg></div>
  <h3>SOLAR ENERGY</h3>
  <p>aut reiciendis voluptatibus maiores alias consequatur aut perferendis doloribus as periores repellat.</p>
  <span class="pill">READ MORE</span>
</div>

<div class="feat-img abs" role="img" aria-label="Battery showing a tree above solar panels"></div>
<svg class="abs" style="left:300px;top:2200px" width="330" height="580" viewBox="0 0 330 580">
  <path d="M40 20 A280 280 0 0 1 40 560" fill="none" stroke="var(--red)" stroke-width="5"/>
  <circle cx="220" cy="90" r="44" fill="var(--red)"/>
  <path d="M224 68 L208 94 H220 L214 114 L232 86 H220 Z" fill="#fff"/>
  <circle cx="294" cy="239" r="46" fill="#fff" stroke="var(--red)" stroke-width="4"/>
  <g fill="none" stroke="var(--red)" stroke-width="2"><circle cx="294" cy="230" r="10"/><path d="M294 240V256M282 256H306M276 230H270M318 230H312M294 212V206"/></g>
  <circle cx="280" cy="407" r="46" fill="#fff" stroke="var(--red)" stroke-width="4"/>
  <g fill="none" stroke="var(--red)" stroke-width="2"><circle cx="276" cy="403" r="12"/><path d="M285 412L298 425"/><circle cx="276" cy="403" r="5"/></g>
</svg>
<div class="feat-title abs">KAVRELON<br><span class="red" style="font-weight:700">CELL FEATURES</span></div>
<div class="feat-item abs" style="left:668px;top:2398px">
  <h4>OUR MISSION</h4>
  <p>Nam libero tempore, cum soluta nobis est eligendi optio cumque nihil impedit quo minus id quod maxime placeat facere possimus, omnis voluptas assumenda est, omnis dolor repellendus.</p>
</div>
<div class="feat-item abs" style="left:653px;top:2563px;width:375px">
  <h4>OUR VISION</h4>
  <p>Nam libero tempore, cum soluta nobis est eligendi optio cumque nihil impedit quo minus id quod maxime placeat facere possimus, omnis voluptas assumenda est, omnis dolor repellendus.</p>
</div>

<section class="solutions abs"></section>
<h2 class="sec abs sol-title">OUR<br><span>SOLUTIONS</span></h2>
<p class="sol-lead abs">Lorem ipsum dolor smet, consectetur adipiscig eit, se od tempor</p>
<span class="more abs" style="left:172px;top:3153px">Read More &rarr;</span>

<div class="sol-card abs" style="left:463px;top:2945px"><span class="num">01</span><svg class="ic" viewBox="0 0 48 48" fill="none" stroke="var(--red)" stroke-width="2"><rect x="4" y="6" width="32" height="26"/><path d="M10 14H30M10 20H24"/><circle cx="34" cy="34" r="8"/></svg><h5>The standard Lorem</h5><p>Lorem ipsum dolor smet, consectetur adipiscig eit, se od tempor incididunt ut labore et dole magna aliqua. Quis ipsum suspendisse</p><span class="more">Read More &rarr;</span></div>
<div class="sol-card abs" style="left:755px;top:2945px"><span class="num">02</span><svg class="ic" viewBox="0 0 48 48" fill="none" stroke="var(--red)" stroke-width="2"><rect x="8" y="10" width="28" height="30"/><path d="M14 4V10M30 4V10M14 20H30M14 28H24"/></svg><h5>The standard Lorem</h5><p>Lorem ipsum dolor smet, consectetur adipiscig eit, se od tempor incididunt ut labore et dole magna aliqua. Quis ipsum suspendisse</p><span class="more">Read More &rarr;</span></div>
<div class="sol-card abs" style="left:172px;top:3250px"><span class="num">03</span><svg class="ic" viewBox="0 0 48 48" fill="none" stroke="var(--red)" stroke-width="2"><rect x="4" y="8" width="36" height="28"/><path d="M10 16H34M10 24H28"/><circle cx="36" cy="36" r="7"/></svg><h5>The standard Lorem</h5><p>Lorem ipsum dolor smet, consectetur adipiscig eit, se od tempor incididunt ut labore et dole magna aliqua. Quis ipsum suspendisse</p><span class="more">Read More &rarr;</span></div>
<div class="sol-card abs" style="left:463px;top:3250px"><span class="num">04</span><svg class="ic" viewBox="0 0 48 48" fill="none" stroke="var(--red)" stroke-width="2"><circle cx="24" cy="18" r="11"/><path d="M18 32H30M19 38H29M24 4V2"/></svg><h5>The standard Lorem</h5><p>Lorem ipsum dolor smet, consectetur adipiscig eit, se od tempor incididunt ut labore et dole magna aliqua. Quis ipsum suspendisse</p><span class="more">Read More &rarr;</span></div>
<div class="sol-card abs" style="left:755px;top:3250px"><span class="num">05</span><svg class="ic" viewBox="0 0 48 48" fill="none" stroke="var(--red)" stroke-width="2"><circle cx="20" cy="20" r="12"/><circle cx="20" cy="20" r="5"/><path d="M28 28L40 40"/></svg><h5>The standard Lorem</h5><p>Lorem ipsum dolor smet, consectetur adipiscig eit, se od tempor incididunt ut labore et dole magna aliqua. Quis ipsum suspendisse</p><span class="more">Read More &rarr;</span></div>

<h2 class="sec abs blog-title">OUR <span>LATEST BLOG</span></h2>
<article class="blog-card abs" style="left:172px">
  <div class="blog-photo" role="img" aria-label="Circuit board with a glowing chip"></div>
  <div class="date">JAN<br>16</div>
  <h6>LOREM IPSUM DOLOR SIT AMET, CONSECTETUR</h6>
  <p>Ut enim ad minim veniam, quis nost rud exercitation ullamco laboris nisi ut aliquip ex ea commodo</p>
</article>
<article class="blog-card abs" style="left:463px">
  <div class="blog-photo b" role="img" aria-label="Rows of battery cells in a pack"></div>
  <div class="date">JAN<br>16</div>
  <h6>LOREM IPSUM DOLOR SIT AMET, CONSECTETUR</h6>
  <p>Ut enim ad minim veniam, quis nost rud exercitation ullamco laboris nisi ut aliquip ex ea commodo</p>
</article>
<article class="blog-card abs" style="left:755px">
  <div class="blog-photo c" role="img" aria-label="Battery module with orange cabling"></div>
  <div class="date">JAN<br>16</div>
  <h6>LOREM IPSUM DOLOR SIT AMET, CONSECTETUR</h6>
  <p>Ut enim ad minim veniam, quis nost rud exercitation ullamco laboris nisi ut aliquip ex ea commodo</p>
</article>
<a class="btn abs load-btn">LOAD MORE</a>

<section class="footer abs"></section>
<svg class="abs" style="left:0;top:4160px" width="1200" height="230" viewBox="0 0 1200 230">
  <path d="M0 230 V205 Q700 215 1200 110 V230 Z" fill="var(--dark)"/>
  <path d="M0 190 Q700 200 1200 0 V70 Q720 215 0 200 Z" fill="var(--red)"/>
</svg>
<div class="foot-brand abs"><div class="dot"></div><div class="name">KAVRELON<br>CELL™</div></div>
<div class="foot-h abs" style="left:495px;top:4464px">QUICK LINKS</div>
<ul class="links abs"><li>Home</li><li>Services</li><li>About Us</li><li>Contact Us</li><li>Blog</li><li>Features</li></ul>
<div class="foot-h abs" style="left:705px;top:4464px">JOIN OUR MAILING LIST AND<br>NEVER MISS AN UPDATE!</div>
<div class="email abs">Email</div>
<a class="btn abs sub">SUBSCRIBE</a>
<svg class="abs" style="left:0;top:4715px" width="1200" height="97" viewBox="0 0 1200 97">
  <path d="M380 0 H1200 V97 H260 Z" fill="var(--red)"/>
</svg>
<div class="copy abs">Copyrights @ 2021 Kavrelon Cell. All Rights Reserved.</div>

</body>
</html>
```